Northern Terrain Published Photographer Website

I need a website to feature a home page slide show of 6 of my top photos then a few simple pages including; gallery, bio, social, checkout, services
Updates

Need extra days to review

Target Market(s)

photography

Industry/Entity Type

Photographer

Coding

Coded - Design and coding required

Number of Pages Required

5+ page

Colors

Designer to choose colors to be used in the design.

Requirements
Must have
• clean eye catching elegant trendy
Nice to have
• unique and creative from other photographer websites

```html
<!DOCTYPE html>
<html lang="en">
<head>
<meta charset="utf-8">
<title>Mara Lindqvist Photography</title>
<link rel="stylesheet" href="https://fonts.googleapis.com/css2?family=Playfair+Display:wght@700;900&family=Lato:wght@400;700&family=Crimson+Text:ital@1&display=swap">
<style>
:root{
  --orange:#ff9900;
  --teal:#0099cc;
  --ink:#111111;
  --grey:#8a8a8a;
  --field-line:#e3e3e3;
  --field-bg:#fcfcfc;
  --white:#ffffff;
}
*{margin:0;padding:0;box-sizing:border-box}
html,body{width:1200px;height:2604px;overflow:hidden;background:var(--white)}
body{position:relative;font-family:"Lato",Arial,sans-serif;color:var(--ink)}
.abs{position:absolute}

/* header */
.top-bar{left:0;top:0;width:1200px;height:62px;background:var(--orange);z-index:3}
.nav-link{top:22px;font-size:16px;color:var(--white);text-decoration:none}
.nav-link.active{font-weight:700}
.brand{left:455px;top:0;width:290px;height:125px;z-index:4}
.brand-name{left:455px;top:0;width:290px;height:125px;display:flex;align-items:center;justify-content:center;gap:10px;z-index:5;color:var(--white);font-family:"Lato",Arial,sans-serif;font-size:22px;font-weight:400;letter-spacing:.5px}
.brand-dot{width:12px;height:12px;border-radius:50%;background:var(--white)}

/* hero */
.hero{left:0;top:62px;width:1200px;height:615px;
  clip-path:polygon(0 0,100% 0,100% 511px,600px 615px,0 511px);
  background:linear-gradient(180deg,#3a3a3b 0%,#4a4641 35%,#6a5747 55%,#2e3e44 75%,#4c4035 100%)}
.hero-title{left:0;top:228px;width:1200px;text-align:center;font-family:"Playfair Display",Georgia,serif;font-weight:700;font-size:64px;line-height:74px;color:var(--teal);z-index:2}
.hero-text{left:0;top:393px;width:1200px;text-align:center;color:var(--white);font-size:17px;line-height:29px;z-index:2}
.btn{background:var(--orange);color:var(--white);font-size:17px;display:flex;align-items:center;justify-content:center;border-radius:2px}
.hero-btn{left:527px;top:479px;width:146px;height:52px;z-index:2}

/* section headings */
.section-title{font-family:"Playfair Display",Georgia,serif;font-weight:700;font-size:42px;color:var(--ink)}
.rule{height:3px;background:var(--ink);width:302px}

/* services */
.service{width:200px}
.service svg{display:block;width:76px;height:76px}
.service-name{margin-top:16px;font-family:"Crimson Text",Georgia,serif;font-style:italic;font-size:26px;color:var(--teal)}
.service-text{margin-top:20px;font-size:14px;line-height:26px;color:var(--grey)}

/* gallery */
.tile{display:block}

/* contact */
.portrait{left:0;top:1948px;width:575px;height:532px;
  clip-path:polygon(0 31px,359px 0,515px 78px,573px 307px,334px 532px,0 532px);
  background:linear-gradient(160deg,#9a9ea4 0%,#d9c7c6 40%,#e6e6e8 65%,#5a5f66 100%)}
.field{left:636px;width:487px;background:var(--field-bg);border:1px solid var(--field-line);border-radius:3px;padding:20px 12px;font-size:14px;color:var(--grey)}
.send-btn{left:636px;top:2427px;width:487px;height:52px}

/* footer */
.footer{left:0;top:2541px;width:1200px;height:63px;background:var(--teal);color:var(--white);font-size:13px;display:flex;align-items:center;justify-content:center}
</style>
</head>
<body>

<header>
  <div class="abs top-bar"></div>
  <a class="abs nav-link active" style="left:221px" href="#">Home</a>
  <a class="abs nav-link" style="left:300px" href="#">Bio</a>
  <a class="abs nav-link" style="left:357px" href="#">Services</a>
  <a class="abs nav-link" style="left:783px" href="#">Gallery</a>
  <a class="abs nav-link" style="left:882px" href="#">Checkout</a>
  <a class="abs nav-link" style="left:991px" href="#">Contact</a>
  <svg class="abs brand" viewBox="0 0 290 125"><polygon points="0,62 42,0 248,0 290,62 248,125 42,125" fill="#000"/></svg>
  <div class="abs brand-name">Mara Lindqvist<span class="brand-dot"></span></div>
</header>

<section>
  <div class="abs hero" role="img" aria-label="Landscape photograph of a canyon lake under stormy clouds"></div>
  <h1 class="abs hero-title">photographer Mara<br>Lindqvist's photography</h1>
  <p class="abs hero-text">Lorem ipsum dolor sit amet, consectetur adipiscing elit sed do<br>eiusmod tempor incididunt ut labore et aliqua.</p>
  <div class="abs btn hero-btn">READ MORE</div>
</section>

<section>
  <h2 class="abs section-title" style="left:80px;top:700px">Our Services</h2>
  <div class="abs rule" style="left:77px;top:771px"></div>

  <div class="abs service" style="left:78px;top:812px">
    <svg viewBox="0 0 76 76" fill="none" stroke="#ff9900" stroke-width="2.5" stroke-linejoin="round"><path d="M2 56 L22 22 L30 30 L42 6 L60 34"/><path d="M14 76 Q20 50 34 40"/><path d="M26 76 Q30 56 40 46"/><path d="M58 38 L50 52 H66 Z M58 48 L48 64 H68 Z M58 64 V72"/></svg>
    <div class="service-name">Nature</div>
    <p class="service-text">Lorem ipsum dolor si amet,<br>&nbsp;dolore magna aliqua.</p>
  </div>
  <div class="abs service" style="left:292px;top:812px">
    <svg viewBox="0 0 76 76" fill="none" stroke="#ff9900" stroke-width="3"><path d="M2 18 V4 H18 M58 4 H72 V18 M72 58 V72 H58 M18 72 H2 V58"/><circle cx="38" cy="24" r="7"/><path d="M10 60 L28 36 L38 48 L48 40 L64 60 Z"/></svg>
    <div class="service-name">Landscape</div>
    <p class="service-text">Lorem ipsum dolor si amet,<br>&nbsp;dolore magna aliqua.</p>
  </div>
  <div class="abs service" style="left:505px;top:812px">
    <svg viewBox="0 0 76 76" role="img" aria-label="Wildlife icon"><rect x="6" y="2" width="50" height="72" rx="20" fill="#ffe2b3"/></svg>
    <div class="service-name">Wildlife</div>
    <p class="service-text">Lorem ipsum dolor si amet,<br>&nbsp;dolore magna aliqua.</p>
  </div>
  <div class="abs service" style="left:718px;top:812px">
    <svg viewBox="0 0 76 76" fill="none" stroke="#ff9900" stroke-width="2.5"><path d="M22 30 A16 16 0 0 1 54 30"/><path d="M38 4 V10 M20 12 L24 17 M56 12 L52 17 M12 26 L18 28 M64 26 L58 28"/><path d="M2 50 Q30 20 74 72"/></svg>
    <div class="service-name">Sunsets</div>
    <p class="service-text">Lorem ipsum dolor si amet,<br>&nbsp;dolore magna aliqua.</p>
  </div>
  <div class="abs service" style="left:932px;top:812px">
    <svg viewBox="0 0 76 76" fill="none" stroke="#ff9900" stroke-width="2.5"><circle cx="38" cy="26" r="11"/><path d="M38 2 V8 M14 10 L19 15 M62 10 L57 15 M4 26 H12 M64 26 H72"/><path d="M2 60 L20 40 L38 60 L56 40 L74 60 M10 72 L26 54 L38 68 L50 54 L66 72"/></svg>
    <div class="service-name">Sunrises</div>
    <p class="service-text">Lorem ipsum dolor si amet,<br>&nbsp;dolore magna aliqua.</p>
  </div>
</section>

<section>
  <h2 class="abs section-title" style="left:80px;top:1065px">Latest Gallery</h2>
  <div class="abs rule" style="left:77px;top:1135px"></div>

  <div class="abs tile" style="left:77px;top:1187px;width:389px;height:209px;background:linear-gradient(180deg,#8a5a8a,#c24aa0 70%,#5a1a6a)" role="img" aria-label="Full moon behind silhouetted trees in a purple sky"></div>
  <div class="abs tile" style="left:477px;top:1187px;width:208px;height:261px;background:linear-gradient(180deg,#6f8050,#9fb56a 50%,#8aa860)" role="img" aria-label="Elk bugling in a green meadow"></div>
  <div class="abs tile" style="left:696px;top:1187px;width:208px;height:156px;background:linear-gradient(180deg,#6c8fb4,#e8884a 55%,#2c3a4a)" role="img" aria-label="Beach pavilion and pier at sunset"></div>
  <div class="abs tile" style="left:915px;top:1187px;width:208px;height:156px;background:linear-gradient(180deg,#f28a2e,#e0521c 60%,#2a1a10)" role="img" aria-label="Lighthouse silhouette against an orange sunset"></div>
  <div class="abs tile" style="left:696px;top:1354px;width:427px;height:427px;background:radial-gradient(circle at 50% 15%,#fff2b0 0%,#f0a020 25%,#b05a08 60%,#3a1a04 100%)" role="img" aria-label="Heron beside pier pilings in golden sunset water"></div>
  <div class="abs tile" style="left:77px;top:1406px;width:389px;height:209px;background:linear-gradient(180deg,#4a4030,#5e5440 50%,#6a9a80 65%,#3e3628)" role="img" aria-label="Forested river gorge from above"></div>
  <div class="abs tile" style="left:477px;top:1458px;width:208px;height:157px;background:linear-gradient(180deg,#8a2a8a,#20181c 35%,#7a6a80 70%,#1a1418)" role="img" aria-label="Waterfall at dusk"></div>
  <div class="abs tile" style="left:77px;top:1625px;width:208px;height:156px;background:linear-gradient(135deg,#d8d8d8,#6a6a6a 55%,#bcbcbc)" role="img" aria-label="Woodpecker on a bare tree"></div>
  <div class="abs tile" style="left:297px;top:1625px;width:208px;height:156px;background:linear-gradient(180deg,#c8ccd8,#2e3e48 45%,#e6eaf0 70%,#4a5a70)" role="img" aria-label="Winter river through snowy forest"></div>
  <div class="abs tile" style="left:515px;top:1625px;width:170px;height:156px;background:linear-gradient(180deg,#3a3018,#e8a030 55%,#201808)" role="img" aria-label="Sunset through tree branches over water"></div>

  <div class="abs btn" style="left:537px;top:1833px;width:125px;height:52px">VIEW ALL</div>
</section>

<section>
  <div class="abs portrait" role="img" aria-label="Portrait of the photographer"></div>
  <h2 class="abs section-title" style="left:638px;top:1940px">Contact Form</h2>
  <div class="abs rule" style="left:635px;top:2010px"></div>
  <div class="abs field" style="top:2052px;height:62px">Your Name :</div>
  <div class="abs field" style="top:2130px;height:62px">Phone :</div>
  <div class="abs field" style="top:2208px;height:62px">Email :</div>
  <div class="abs field" style="top:2286px;height:124px">Message / Comments :</div>
  <div class="abs btn send-btn">SEND MESSAGE</div>
</section>

<footer class="abs footer">Copyright ©&nbsp;<b>Mara Lindqvist</b>&nbsp;- 2019 . All Right Reserved</footer>

</body>
</html>
```